GHalvor Busisness Card

I am an aerospace consultant and at this time only need business cards.

Industry/Entity Type

Business

Contact Information for Business Card

Halvorsen Associates,LLC
Marcus D. Halvorsen

348 Birch Meadow Drive
Hartwell AL 35612

256-555-0187 (cell)
256-555-0142 (fax)

marcushalvorsen@mailbrook.test

```html
<!DOCTYPE html>
<html lang="en">
<head>
<meta charset="utf-8">
<title>Halvorsen Associates – Business Card</title>
<link href="https://fonts.googleapis.com/css2?family=Lato:wght@400;700;900&display=swap" rel="stylesheet">
<style>
  :root {
    --backdrop: #2b2b2b;
    --card: #f7f7f7;
    --brand-red: #d10a10;
    --deep-red: #a8060b;
    --ink: #1c1c1c;
  }
  html, body {
    margin: 0;
    width: 1200px;
    height: 900px;
    overflow: hidden;
    background: var(--backdrop);
    font-family: "Lato", sans-serif;
  }
  .card {
    position: absolute;
    left: 75px;
    top: 150px;
    width: 1050px;
    height: 600px;
    background: var(--card);
    overflow: hidden;
  }
  .card-bands {
    position: absolute;
    inset: 0;
  }
  .holder {
    position: absolute;
    left: 70px;
    top: 62px;
  }
  .holder-name {
    margin: 0;
    color: var(--brand-red);
    font-weight: 900;
    font-size: 40px;
    letter-spacing: 1px;
    text-transform: uppercase;
    line-height: 1.1;
  }
  .holder-title {
    margin: 2px 0 0;
    color: var(--ink);
    font-weight: 700;
    font-size: 24px;
  }
  .company {
    position: absolute;
    left: 0;
    right: 0;
    top: 220px;
    text-align: center;
  }
  .company-name {
    margin: 0;
    color: var(--brand-red);
    font-weight: 900;
    font-size: 56px;
    letter-spacing: 1px;
    line-height: 1;
    padding: 22px 0;
  }
  .rule {
    position: absolute;
    height: 4px;
    width: 520px;
    background: linear-gradient(90deg, transparent, var(--brand-red) 70%, transparent);
  }
  .rule-top { top: 0; left: 300px; }
  .rule-bottom { bottom: 0; left: 240px; }
  .contact {
    position: absolute;
    font-weight: 700;
    color: var(--ink);
    font-size: 25px;
  }
  .contact-line {
    display: flex;
    align-items: center;
    gap: 10px;
    margin-bottom: 8px;
    white-space: nowrap;
  }
  .contact-primary {
    right: 470px;
    top: 420px;
    text-align: right;
  }
  .contact-primary .contact-line { justify-content: flex-end; }
  .contact-secondary {
    left: 610px;
    top: 380px;
  }
  .icon { width: 26px; height: 26px; flex: none; }
</style>
</head>
<body>
  <section class="card" aria-label="Business card for Halvorsen Associates">
    <svg class="card-bands" viewBox="0 0 1050 600" aria-hidden="true">
      <path d="M0 0 H770 C735 0 725 30 690 30 H0 Z" fill="var(--brand-red)"/>
      <path d="M1050 600 H260 C300 600 305 545 350 545 H1050 Z" fill="var(--deep-red)"/>
    </svg>

    <header class="holder">
      <h1 class="holder-name">Marcus D. Halvorsen</h1>
      <p class="holder-title">Aerospace Consultant</p>
    </header>

    <div class="company">
      <span class="rule rule-top"></span>
      <h2 class="company-name">HALVORSEN ASSOCIATES</h2>
      <span class="rule rule-bottom"></span>
    </div>

    <div class="contact contact-primary">
      <div class="contact-line">256-555-0187
        <svg class="icon" viewBox="0 0 24 24" aria-label="cell"><rect x="6" y="2" width="12" height="20" rx="2" fill="none" stroke="var(--brand-red)" stroke-width="2"/><circle cx="12" cy="18" r="1.2" fill="var(--brand-red)"/></svg>
      </div>
      <div class="contact-line">348 Birch Meadow Drive Hartwell AL 35612
        <svg class="icon" viewBox="0 0 24 24" aria-label="address"><path d="M12 3 L2 12 H5 V21 H10 V15 H14 V21 H19 V12 H22 Z" fill="var(--brand-red)"/></svg>
      </div>
    </div>

    <div class="contact contact-secondary">
      <div class="contact-line">
        <svg class="icon" viewBox="0 0 24 24" aria-label="fax"><rect x="7" y="3" width="10" height="6" fill="var(--brand-red)"/><rect x="3" y="9" width="18" height="9" rx="2" fill="var(--brand-red)"/><rect x="7" y="14" width="10" height="7" fill="#fff" stroke="var(--brand-red)" stroke-width="2"/></svg>
        256-555-0142
      </div>
      <div class="contact-line">
        <svg class="icon" viewBox="0 0 24 24" aria-label="email"><rect x="2" y="5" width="20" height="14" fill="var(--brand-red)"/><path d="M3 6 L12 13 L21 6" fill="none" stroke="#fff" stroke-width="2"/></svg>
        marcushalvorsen@mailbrook.test
      </div>
    </div>
  </section>
</body>
</html>
```